I would like to incoroporate some of the photos attached for a design on a 4x6 postcard. This is for a design/build company called Tom Brenner Garden Design. We design the landscape or garden and install it. The phone number, I want to use is 555-318-2760. I want the design to make someone want to call imediately for a landscape makeover. I have attached several photos of work we have done. I would rather not use other images of other peoples work, but am open to ideas. Want to keep wording to a mininum since the name pretty much says it all and focus on a creative design incorporating garden design photos.
I would like at the bottom of the page something that says something to the effect of: "Find some of our completed design under YardCraft on Friendbook or yardcraft.example
The post card will be two sided

```html
<!DOCTYPE html>
<html lang="en">
<head>
<meta charset="utf-8">
<title>Tom Brenner Garden Design – Postcard</title>
<link href="https://fonts.googleapis.com/css2?family=Poiret+One&family=Sniglet:wght@400;800&display=swap" rel="stylesheet">
<style>
  :root {
    --page: #ffffff;
    --card-edge: #6f6f6f;
    --blush: #e9dcdc;
    --ink: #111111;
    --white: #ffffff;
    --rule: #222222;
    --stamp: #9a9a9a;
  }
  * { box-sizing: border-box; margin: 0; padding: 0; }
  html, body { width: 883px; height: 1200px; overflow: hidden; background: var(--page); }
  .sheet { position: relative; width: 883px; height: 1200px; }

  .card {
    position: absolute; left: 47px; width: 792px; height: 526px;
    border: 1px solid var(--card-edge); background: var(--white); overflow: hidden;
  }
  .card--front { top: 54px; }
  .card--back  { top: 637px; background: var(--blush); }

  .photo {
    position: absolute; border-radius: 6px;
    box-shadow: inset 0 0 10px 8px rgba(255,255,255,0.9), 0 0 0 6px rgba(255,255,255,0.85);
  }
  .photo--bed-corner   { left: 14px;  top: 8px;   width: 290px; height: 215px;
    background: radial-gradient(ellipse at 55% 65%, #d86aa0 0%, #6f9a3a 30%, #3d5a2a 70%, #2e3a26 100%); }
  .photo--front-border { left: 380px; top: 8px;   width: 395px; height: 300px;
    background: linear-gradient(180deg, #8a8276 0%, #4f6a3a 45%, #c83a4a 65%, #a4c64a 80%, #d9d6cc 100%); }
  .photo--hydrangea    { left: 14px;  top: 248px; width: 410px; height: 266px;
    background: linear-gradient(160deg, #54583a 0%, #2f4a2a 35%, #e8ecd8 60%, #8a9a6a 80%, #8a5a4a 100%); }
  .photo--pansy-lawn   { left: 448px; top: 334px; width: 308px; height: 167px;
    background: linear-gradient(180deg, #5e7a3e 0%, #3f6a2e 45%, #6a4aa0 70%, #e0c030 100%); }

  .front-note {
    position: absolute; left: 0; right: 0; top: 372px; text-align: center;
    font-family: "Sniglet", sans-serif; font-weight: 800; font-size: 25px; line-height: 48px;
    color: var(--white);
    text-shadow: -1.5px -1.5px 0 var(--ink), 1.5px -1.5px 0 var(--ink), -1.5px 1.5px 0 var(--ink), 1.5px 1.5px 0 var(--ink), 0 2px 0 var(--ink);
  }

  .brush { position: absolute; background: var(--white); border-radius: 40px; opacity: 0.92; }
  .brush--a { left: -20px; top: 150px; width: 420px; height: 420px; border-radius: 0 200px 0 0; opacity: 0.7; }
  .brush--b { left: 300px; top: 70px;  width: 520px; height: 90px;  transform: rotate(-2deg); opacity: 0.55; }
  .brush--c { left: 370px; top: 300px; width: 460px; height: 70px;  opacity: 0.75; }
  .brush--d { left: 380px; top: 410px; width: 440px; height: 60px;  transform: rotate(1deg); opacity: 0.85; }
  .brush--e { left: 60px;  top: 440px; width: 700px; height: 90px;  opacity: 0.9; }

  .brand {
    position: absolute; left: 50px; top: 46px; width: 400px; text-align: center;
    font-family: "Poiret One", sans-serif; font-size: 46px; line-height: 52px; color: var(--ink);
  }
  .stamp { position: absolute; left: 673px; top: 51px; width: 67px; height: 82px; }

  .photo--porch { left: 62px; top: 190px; width: 270px; height: 208px;
    background: linear-gradient(180deg, #6a7380 0%, #b8a48a 35%, #e8e4dc 50%, #c02830 68%, #9cc040 82%, #cfc4a8 100%); }

  .address-lines { position: absolute; left: 378px; top: 232px; width: 374px; }
  .address-lines span { display: block; height: 47px; border-bottom: 1.5px solid var(--rule); }

  .contact { position: absolute; left: 120px; top: 454px; display: flex; align-items: baseline; gap: 34px; }
  .contact__label { font-family: "Poiret One", sans-serif; font-size: 24px; color: var(--ink); }
  .contact__phone { font-family: "Sniglet", sans-serif; font-weight: 800; font-size: 60px; letter-spacing: 2px; color: var(--ink); }
</style>
</head>
<body>
<main class="sheet">

  <section class="card card--front" aria-label="Postcard front">
    <div class="photo photo--bed-corner" role="img" aria-label="Photo of a corner garden bed with caladiums and pink flowers"></div>
    <div class="photo photo--front-border" role="img" aria-label="Photo of a house front with red and pink flower border"></div>
    <div class="photo photo--hydrangea" role="img" aria-label="Photo of white hydrangeas with evergreen shrubs"></div>
    <div class="photo photo--pansy-lawn" role="img" aria-label="Photo of a lawn with purple and yellow pansy bed"></div>
    <p class="front-note">Find some of our completed design under<br>YardCraft on Friendbook or yardcraft.example</p>
  </section>

  <section class="card card--back" aria-label="Postcard back">
    <div class="brush brush--a"></div>
    <div class="brush brush--b"></div>
    <div class="brush brush--c"></div>
    <div class="brush brush--d"></div>
    <div class="brush brush--e"></div>

    <h1 class="brand">Tom Brenner Garden<br>Design</h1>

    <svg class="stamp" viewBox="0 0 67 82" aria-hidden="true">
      <rect x="3" y="3" width="61" height="76" fill="none" stroke="var(--stamp)" stroke-width="1.5" stroke-dasharray="3 2"/>
    </svg>

    <div class="photo photo--porch" role="img" aria-label="Photo of a porch home with curved walkway and red flower beds"></div>

    <div class="address-lines" aria-hidden="true"><span></span><span></span><span></span><span></span></div>

    <p class="contact">
      <span class="contact__label">Contact us</span>
      <span class="contact__phone">555-318-2760</span>
    </p>
  </section>

</main>
</body>
</html>
```